Ranked amongst the Best Colleges and Programs

the size of the ad is Full Page, with bleed*
8”x 10.75" plus 0.25" bleed'
you have two choices for the tagline .. please chose what ever you think will allow you to make a better ad.
The instructions on the brief are in red
I am looking for a hight quality modern ad to place in local weekly publications that will stand out .
I would like a ad that people will look at and say i would like to see what this ad is all about.
I apprecate creative work.
the ad should not be very crowded and the text should be able to be read.
if you decide to use people in the ad .. (you don't have to ) then it should be a male dressed in white shirt in and sports jacket.. or if you would like you can use a vector and then use male or female people.
please leave one inch on the bottom for the footer

Target Market(s)

potential middle class students from 23-35 years of age

Industry/Entity Type

education

Requirements
Must have
• .the " 98% employment rate" should stand out in the ad.. but should not be the main part of the ad
Nice to have
• creative
Should not have
• Should not be a very busy or crowded ad.. i prefer pictures of men but should be .. in a business suit .. that looks professional- white shirt

```html
<!DOCTYPE html>
<html lang="en">
<head>
<meta charset="UTF-8">
<title>NVU Masters of Accounting – Full Page Ad</title>
<link href="https://fonts.googleapis.com/css2?family=Anton&family=Montserrat:wght@500;600;800;900&display=swap" rel="stylesheet">
<style>
  :root {
    --backdrop: #f1f0ee;
    --orange: #e0852a;
    --amber: #eaa52a;
    --sun: #f0c72c;
    --frame-yellow: #f7e23a;
    --crimson: #ae222d;
    --ink: #111111;
    --paper: #e3e3e3;
    --paper-edge: #f7f7f7;
    --white: #ffffff;
  }
  * { margin: 0; padding: 0; box-sizing: border-box; }
  html, body { width: 1200px; height: 801px; overflow: hidden; background: var(--backdrop); }
  .ad {
    position: absolute; left: 333px; top: 20px; width: 533px; height: 761px;
    background: var(--paper); overflow: hidden;
    font-family: "Montserrat", sans-serif; color: var(--ink);
    box-shadow: 0 4px 18px rgba(0,0,0,0.12);
  }
  .hero {
    position: absolute; left: 0; top: 0; width: 100%; height: 366px;
    background: radial-gradient(ellipse at 70% 95%, var(--sun) 0%, var(--amber) 45%, var(--orange) 100%);
  }
  .hero-frame {
    position: absolute; left: 32px; top: 32px; width: 466px; height: 285px;
    border: 2px solid var(--frame-yellow); border-radius: 14px;
  }
  .paper-edge {
    position: absolute; left: 0; top: 354px; width: 100%; height: 22px;
  }
  .headline-line {
    position: absolute; left: 0; width: 100%; text-align: center;
    font-family: "Anton", sans-serif; text-transform: uppercase; line-height: 1;
  }
  .headline-dark { color: var(--ink); font-size: 42px; }
  .headline-accent { color: var(--white); text-shadow: 2px 3px 3px rgba(0,0,0,0.35); }
  .line-small { top: 56px; font-size: 30px; }
  .line-invest { top: 106px; }
  .line-big { top: 156px; font-size: 72px; }
  .line-diff { top: 244px; }
  .brush { position: absolute; }
  .program-tag {
    position: absolute; left: 135px; top: 304px; width: 258px; height: 26px;
    border: 2px solid var(--frame-yellow); border-radius: 13px;
    background: linear-gradient(90deg, var(--amber), var(--sun));
    font-size: 14px; font-weight: 500; text-align: center; line-height: 22px;
  }
  .stat-blob { position: absolute; left: 25px; top: 393px; width: 231px; height: 182px; }
  .stat-value {
    position: absolute; left: 25px; top: 440px; width: 231px; text-align: center;
    font-weight: 900; font-size: 56px; color: var(--white); line-height: 1; letter-spacing: -1px;
  }
  .stat-value sup { font-size: 26px; vertical-align: 22px; }
  .stat-label {
    position: absolute; left: 77px; top: 502px; width: 129px; height: 16px;
    border: 1px solid var(--white); color: var(--white);
    font-size: 9px; font-weight: 800; text-align: center; line-height: 14px; letter-spacing: 0.2px;
  }
  .divider-dotted {
    position: absolute; left: 271px; top: 433px; height: 117px;
    border-left: 1px dotted #555;
  }
  .ranked-tag {
    position: absolute; left: 293px; top: 428px; width: 152px; height: 26px;
    background: var(--amber); clip-path: polygon(2% 8%, 98% 0, 100% 55%, 97% 100%, 0 92%, 1% 45%);
    font-size: 11.5px; font-weight: 600; line-height: 26px; padding-left: 10px;
  }
  .ranking { position: absolute; left: 293px; }
  .ranking-list { font-size: 12.5px; font-weight: 500; }
  .ranking-source { font-size: 21px; font-weight: 800; color: var(--crimson); line-height: 1; }
  .ranking-rule { position: absolute; left: 293px; top: 509px; width: 208px; border-top: 1px solid #555; }
  .outcomes {
    position: absolute; left: 0; top: 590px; width: 100%; text-align: center;
    font-size: 10.5px; font-weight: 500; line-height: 13.5px;
  }
  .footer-rule { position: absolute; left: 25px; top: 628px; width: 477px; border-top: 1px solid var(--ink); }
</style>
</head>
<body>
<main class="ad">
  <section class="hero">
    <div class="hero-frame"></div>

    <svg class="brush" style="left:197px;top:55px" width="137" height="45" role="img" aria-label="Red brush stroke behind the words A Small">
      <polygon points="6,8 128,2 137,22 130,42 10,45 0,26" fill="var(--crimson)"/>
    </svg>
    <svg class="brush" style="left:162px;top:154px" width="206" height="84" role="img" aria-label="Red brush stroke behind the words A Big">
      <polygon points="12,10 190,0 206,40 196,80 18,84 0,44" fill="var(--crimson)"/>
    </svg>

    <h1>
      <span class="headline-line headline-accent line-small">A Small</span>
      <span class="headline-line headline-dark line-invest">Investment Today,</span>
      <span class="headline-line headline-accent line-big">A Big</span>
      <span class="headline-line headline-dark line-diff">Difference Tomorrow</span>
    </h1>

    <div class="program-tag">NVU- Masters of Accounting</div>
  </section>

  <svg class="paper-edge" viewBox="0 0 533 22" preserveAspectRatio="none" role="img" aria-label="Torn paper edge">
    <rect x="0" y="0" width="533" height="22" fill="var(--paper-edge)"/>
  </svg>

  <svg class="stat-blob" viewBox="0 0 231 182" role="img" aria-label="Red brush splash behind the employment figure">
    <polygon points="30,40 110,0 200,30 231,130 150,182 40,160 0,90" fill="var(--crimson)"/>
  </svg>
  <div class="stat-value">98<sup>%</sup></div>
  <div class="stat-label">EMPLOYMENT RATE</div>

  <div class="divider-dotted"></div>

  <div class="ranked-tag">Ranked amongst:</div>
  <p class="ranking ranking-list" style="top:462px">Best Colleges</p>
  <p class="ranking ranking-source" style="top:480px">Ledgerline 2023</p>
  <div class="ranking-rule"></div>
  <p class="ranking ranking-list" style="top:514px">Best Masters in Accounting</p>
  <p class="ranking ranking-source" style="top:532px">Academica 2023</p>

  <p class="outcomes">NVU graduates have gone on to work in various high-quality jobs in top firms,<br>earning impressive six-figure salaries as well as opening successful businesses.</p>
  <div class="footer-rule"></div>
</main>
</body>
</html>
```